Veterinary Pylon

My veterinary clinic is not clearly visible from the street and I want to place a Pylon next to my driveway. I want a modern, elegant straight Design, the Photo shows the sheduled place. One can see the clinic on our Homepage: www.fernhollow-tierpraxis.at
The last pictures are examples for pylones I like

Target Market(s)

the passing cars often miss my entry...I want to show where to turn left

Colors
3276b5
33a6d7
00a990

Requirements
Must have
• High value, simple elegance, size: 250cm (high) x 100cm (width)
Nice to have
• Our Logo, arrow(?)

A special Text is not necessary but this will be an option:

Biegen sie hier ab und wir biegen es wieder hin!
Should not have
• Too much Color, the colors I have chosen are the possible colors but it‘s not necessary to use them.

```html
<!DOCTYPE html>
<html lang="de">
<head>
<meta charset="utf-8">
<title>Fernhollow Tierpraxis – Pylon</title>
<link rel="stylesheet" href="https://fonts.googleapis.com/css2?family=Open+Sans:wght@800&family=Raleway:wght@600;800&display=swap">
<style>
  :root {
    --page-bg: #e9eaec;
    --panel-white: #f6f7f9;
    --navy: #1b3f8f;
    --deep-blue: #0b3a8c;
    --mid-blue: #1f5fbd;
    --sky-blue: #33a6d7;
    --pill-blue: #8fd0ee;
    --ink: #16181c;
    --white: #ffffff;
  }
  * { box-sizing: border-box; margin: 0; padding: 0; }
  html, body { width: 796px; height: 1200px; overflow: hidden; background: var(--page-bg); }
  .canvas { position: relative; width: 796px; height: 1200px; }

  /* 100 cm x 250 cm pylon face, scaled to 440 x 1100 px */
  .pylon {
    position: absolute;
    left: 178px; top: 50px;
    width: 440px; height: 1100px;
    background: linear-gradient(170deg, var(--white) 0%, var(--panel-white) 55%, #e8ecf1 100%);
    box-shadow: 6px 8px 16px rgba(0,0,0,0.28);
    overflow: hidden;
  }
  .pylon__waves { position: absolute; inset: 0; width: 100%; height: 100%; }

  .brand {
    position: absolute;
    left: 0; right: 0; top: 90px;
    display: flex; flex-direction: column; align-items: center; gap: 26px;
  }
  .brand__dot {
    width: 110px; height: 110px; border-radius: 50%;
    background: var(--navy);
  }
  .brand__name {
    font-family: "Raleway", sans-serif;
    font-weight: 800;
    color: var(--navy);
    font-size: 46px;
    line-height: 1.05;
    letter-spacing: 1px;
    text-transform: uppercase;
    text-align: center;
  }

  .turn-arrow {
    position: absolute;
    left: 90px; top: 430px;
    width: 260px; height: 150px;
  }

  .phone {
    position: absolute;
    left: 30px; top: 790px;
    width: 380px; height: 66px;
    border-radius: 33px;
    background: var(--pill-blue);
    display: flex; align-items: center;
    padding-left: 9px; gap: 16px;
  }
  .phone__icon {
    width: 48px; height: 48px; border-radius: 50%;
    background: var(--navy);
    display: flex; align-items: center; justify-content: center;
    flex: none;
  }
  .phone__number {
    font-family: "Open Sans", sans-serif;
    font-weight: 800;
    font-size: 36px;
    color: var(--ink);
    white-space: nowrap;
  }

  .website {
    position: absolute;
    left: 0; right: 0; top: 890px;
    text-align: center;
    font-family: "Raleway", sans-serif;
    font-weight: 600;
    font-size: 25px;
    color: var(--white);
    white-space: nowrap;
  }
</style>
</head>
<body>
<main class="canvas">
  <section class="pylon" aria-label="Pylon Fernhollow Tierpraxis">
    <svg class="pylon__waves" viewBox="0 0 440 1100" aria-hidden="true">
      <defs>
        <linearGradient id="waveBlue" x1="0" y1="0" x2="1" y2="1">
          <stop offset="0" stop-color="#1f5fbd"/>
          <stop offset="0.55" stop-color="#0b3a8c"/>
          <stop offset="1" stop-color="#1a56b0"/>
        </linearGradient>
      </defs>
      <path d="M0,660 C90,720 180,760 280,748 C360,738 400,700 440,688 L440,1100 L0,1100 Z" fill="url(#waveBlue)"/>
      <path d="M0,656 C90,714 180,754 280,742 C360,732 400,696 440,684" fill="none" stroke="#33a6d7" stroke-width="4"/>
      <path d="M250,772 C340,764 400,728 440,716" fill="none" stroke="#33a6d7" stroke-width="6" opacity="0.8"/>
      <path d="M0,960 C60,1000 100,1060 140,1100 L0,1100 Z" fill="#33a6d7" opacity="0.55"/>
      <path d="M180,1100 C280,1080 370,1030 440,1010 L440,1100 Z" fill="#33a6d7" opacity="0.35"/>
    </svg>

    <div class="brand">
      <span class="brand__dot"></span>
      <span class="brand__name">Fernhollow<br>Tierpraxis</span>
    </div>

    <svg class="turn-arrow" viewBox="0 0 260 150" role="img" aria-label="Pfeil nach links: hier abbiegen">
      <polygon points="0,75 90,0 90,45 260,45 260,105 90,105 90,150" fill="#1b3f8f"/>
      <rect x="110" y="128" width="150" height="6" fill="#33a6d7"/>
    </svg>

    <div class="phone">
      <span class="phone__icon">
        <svg width="26" height="26" viewBox="0 0 24 24" aria-hidden="true">
          <path d="M6.6 10.8a15.1 15.1 0 0 0 6.6 6.6l2.2-2.2a1 1 0 0 1 1-.25 11.4 11.4 0 0 0 3.6.57 1 1 0 0 1 1 1V20a1 1 0 0 1-1 1A17 17 0 0 1 3 4a1 1 0 0 1 1-1h3.5a1 1 0 0 1 1 1c0 1.25.2 2.45.57 3.57a1 1 0 0 1-.25 1z" fill="#ffffff"/>
        </svg>
      </span>
      <span class="phone__number">(0316) 482 917</span>
    </div>

    <p class="website">www.fernhollow-tierpraxis.at</p>
  </section>
</main>
</body>
</html>
```